Letterhead needed using basic elements of our new logo!

We have just had a new logo and business card created on Pixel Harbor and now would like a new letterhead for our company re-branding. Our logo inspires trust, professionalism and confidence and we would like to mirror that in our letterhead. We would like to use elements in our logo (as well as the logo itself, obviously), but understand with only a header and the ability to print in black and white, we are somewhat limited. We have also won the Resident's Pick Medal for best Property Management Company in our city and would like to somehow include that small banner (see uploaded file) in the letterhead, without it clashing?

Text to include:
Stonebrook Property Management (and logo)
C-214 Marlowe Ave, Winnipeg, MB R2K 3P7
Ph: 204-738-2915
Fax: 1-888-276-9413
Email: customerservice@stonebrookpropertymanagement.example
Web: www.stonebrookpropertymanagement.example

Pasted below is our mission, vision and branding statements to help with the project:

Mission Statement

Provide the highest quality customer service to both property owners and tenants using innovative technology and well trained, caring staff.

Vision Statement

To redefine the way in which management is delivered to its customers, becoming the recognized leader in the property management industry.

Brand Essence

When our customers experience our product or service, it brings forth an emotion of absolute trust that we have their best interests at heart

Brand Personality

We are a company that is passionate about our customers, our company and our vision to be leaders in the field of property management. We are visionaries that aren't afraid to use cutting edge technologies to improve our products and service.

Position or Value Proposition

To whom are we speaking?
- real estate investors, including first timers that are giving us their first starter home. They are fairly naive, as they are not "big time" investors, and because they are giving us their first home (in contract to an investor buying a rental property, often sight unseen) they are more emotionally tied to their property and will require a company that inspires trust and confidence.

What is our brand promise?
- we will do our best to serve our clients, both owners and tenants, to give them prompt communication, clear, concise answers to their questions, and look after their property quickly and competently.

Why is our product different than the competition and why should our customers care?
- the current model used by most management companies employs individual portfolio managers that do things a little differently each instance, and differently than their fellow staff members. Our management product is superior because we use a combination of technology and strict procedures to ensure each client's experience is consistent, each and every time.

Industry/Entity Type

Business

Requirements
Must have
• We would like an option to be in black and white, to be able to be printed from Microsoft Word. As well, we do not want anything in a footer or any other kind of letterhead that bleeds below a header. The main use of this letterhead will be from our property management software, to be used in our form letters and other templates (sent to tenants and clients)
Should not have
• Footer or other elements where the text body would be, it will be used in a form letter

```html
<!DOCTYPE html>
<html lang="en">
<head>
<meta charset="utf-8">
<title>Stonebrook Property Management – Letterhead</title>
<link href="https://fonts.googleapis.com/css2?family=Carlito:wght@400;700&display=swap" rel="stylesheet">
<style>
  :root {
    --backdrop: #e8eaed;
    --paper: #ffffff;
    --brand-blue: #1e9ad6;
    --ink: #3a3a3a;
    --body-grey: #8a8a8a;
    --contact-grey: #555555;
    --caption-ink: #222222;
  }
  * { margin: 0; padding: 0; box-sizing: border-box; }
  html, body { width: 1000px; height: 1200px; overflow: hidden; }
  body {
    background: var(--backdrop);
    font-family: "Carlito", "Calibri", sans-serif;
    position: relative;
  }
  .letterhead {
    position: absolute;
    left: 154px; top: 111px;
    width: 692px; height: 979px;
    background: var(--paper);
    overflow: hidden;
  }
  .brand {
    position: absolute; left: 66px; top: 72px;
    display: flex; align-items: center; gap: 10px;
  }
  .brand-mark {
    width: 34px; height: 34px; background: var(--brand-blue);
  }
  .brand-name { color: var(--brand-blue); font-weight: 700; line-height: 1; }
  .brand-name .primary { display: block; font-size: 27px; letter-spacing: 1px; text-transform: uppercase; }
  .brand-name .secondary { display: block; font-size: 8.5px; letter-spacing: 2.6px; text-transform: uppercase; margin-top: 3px; }

  .contact {
    position: absolute; left: 452px; top: 75px;
    font-size: 7.4px; color: var(--contact-grey); line-height: 10.4px;
    list-style: none;
  }
  .contact li { display: flex; align-items: center; gap: 5px; white-space: nowrap; }
  .contact .spacer { height: 3px; }
  .contact svg { width: 8px; height: 8px; flex: none; }

  .salutation {
    position: absolute; left: 66px; top: 210px;
    font-size: 14.5px; color: var(--body-grey); line-height: 19px;
  }
  .letter-body {
    position: absolute; left: 66px; top: 265px; width: 556px;
    font-size: 12.6px; line-height: 15.3px; color: var(--body-grey);
  }
  .letter-body p + p { margin-top: 15px; }
  .letter-body p.opening { text-indent: 125px; }

  .signatory { position: absolute; left: 66px; top: 750px; }
  .signatory .name { font-size: 23px; color: var(--ink); line-height: 28px; }
  .signatory .closing { margin-top: 12px; font-size: 9px; color: var(--caption-ink); line-height: 12px; }

  .date {
    position: absolute; right: 70px; top: 802px;
    font-size: 9px; color: var(--caption-ink);
  }
</style>
</head>
<body>
  <main class="letterhead">
    <header>
      <div class="brand">
        <span class="brand-mark" aria-hidden="true"></span>
        <div class="brand-name">
          <span class="primary">Stonebrook</span>
          <span class="secondary">Property Management</span>
        </div>
      </div>
      <ul class="contact">
        <li>
          <svg viewBox="0 0 10 10" aria-hidden="true"><circle cx="5" cy="5" r="4.3" fill="none" stroke="#1e9ad6" stroke-width="1"/><path d="M5 2.6a1.6 1.6 0 0 0-1.6 1.6c0 1.2 1.6 3 1.6 3s1.6-1.8 1.6-3A1.6 1.6 0 0 0 5 2.6z" fill="#1e9ad6"/></svg>
          C-214 Marlowe Ave, Winnipeg, MB R2K 3P7
        </li>
        <li class="spacer"></li>
        <li>
          <svg viewBox="0 0 10 10" aria-hidden="true"><circle cx="5" cy="5" r="4.3" fill="none" stroke="#1e9ad6" stroke-width="1"/><path d="M3.2 3.2l1 0 .5 1.2-.6.5a3 3 0 0 0 1.2 1.2l.5-.6 1.2.5v1c-2.4.2-4.1-1.5-3.8-3.8z" fill="#1e9ad6"/></svg>
          Ph: 204-738-2915
        </li>
        <li>
          <svg viewBox="0 0 10 10" aria-hidden="true"><circle cx="5" cy="5" r="4.3" fill="none" stroke="#1e9ad6" stroke-width="1"/><rect x="3" y="3.4" width="4" height="3.2" fill="#1e9ad6"/></svg>
          Fax: 1-888-276-9413
        </li>
        <li class="spacer"></li>
        <li>customerservice@stonebrookpropertymanagement.example</li>
        <li>www.stonebrookpropertymanagement.example</li>
      </ul>
    </header>

    <p class="salutation">Lorem<br>ipsum dolor sit amet,</p>

    <section class="letter-body">
      <p class="opening">Sed ut perspiciatis unde omnis iste natus error sit voluptatem accusantium doloremque laudantium, totam rem aperiam, eaque ipsa quae ab illo inventore veritatis et quasi architecto beatae vitae dicta sunt explicabo. Nemo enim ipsam voluptatem quia voluptas sit aspernatur aut odit aut fugit, sed quia consequuntur magni dolores eos qui ratione voluptatem sequi nesciunt. Neque porro quisquam est, qui dolorem ipsum quia dolor sit amet, consectetur, adipisci velit, sed quia non numquam eius modi tempora incidunt ut labore et dolore magnam aliquam quaerat voluptatem. Ut enim ad minima veniam, quis nostrum exercitationem ullam corporis suscipit laboriosam, nisi ut aliquid ex ea commodi consequatur? Quis autem vel eum iure reprehenderit qui in ea voluptate velit esse quam nihil molestiae consequatur, vel illum qui dolorem eum fugiat quo voluptas nulla pariatur.</p>
      <p>Sed ut perspiciatis unde omnis iste natus error sit voluptatem accusantium doloremque laudantium, totam rem aperiam, eaque ipsa quae ab illo inventore veritatis et quasi architecto beatae vitae dicta sunt explicabo. Nemo enim ipsam voluptatem quia voluptas sit aspernatur aut odit aut fugit, sed quia consequuntur magni dolores eos qui ratione voluptatem sequi nesciunt. Neque porro quisquam est, qui dolorem ipsum quia dolor sit amet, consectetur, adipisci velit, sed quia non numquam eius modi tempora incidunt ut labore et dolore magnam aliquam quaerat voluptatem. Ut enim ad minima veniam, quis nostrum exercitationem ullam corporis suscipit laboriosam, nisi ut aliquid ex ea commodi consequatur? Quis autem vel eum iure reprehenderit qui in ea voluptate velit esse quam nihil molestiae consequatur, vel illum qui dolorem eum fugiat quo voluptas nulla pariatur. Sed ut perspiciatis unde omnis iste natus error sit voluptatem accusantium doloremque laudantium, totam rem aperiam, eaque ipsa quae ab illo inventore veritatis et quasi architecto beatae vitae dicta sunt explicabo. Nemo enim ipsam voluptatem quia voluptas sit aspernatur aut odit aut fugit, sed quia consequuntur magni dolores eos qui ratione voluptatem sequi nesciunt. Neque porro quisquam est, qui dolorem ipsum quia dolor sit amet, consectetur, adipisci velit, sed quia non numquam eius modi tempora incidunt ut labore et dolore magnam aliquam quaerat voluptatem. Ut enim ad minima veniam, quis nostrum exercitationem ullam corporis suscipit laboriosam, nisi ut aliquid ex ea commodi consequatur? Quis autem vel eum iure reprehenderit qui in ea voluptate velit esse quam nihil molestiae consequatur, vel illum qui dolorem eum fugiat quo voluptas nulla pariatur.</p>
    </section>

    <footer class="signatory">
      <p class="name">John Doe</p>
      <p class="closing">Sincerely,<br>Managing Director</p>
    </footer>
    <p class="date">Date: 01 Jan, 2016</p>
  </main>
</body>
</html>
```